Software Company Requires Website

We need a web design for a new mobile software development company based in London named Velquin Solutions.
The design needs to be clean and smooth. Not too flashy, not too boring.
I would like to try the design with some warm colors, and maybe a headline or something highlighted with a strong color. ( logo ? ) The layout should be something like the bellow links, all in one page.

http://brantelo.net/
http://www.kelvory.com/
http://www.work-plover.de/
http://www.tusker.com/
http://www.quildenta.com/us/

Now some of them they seem different from the others, but in each of them there is something that ticks my brain, so it`s up to you to surprise me.

I have uploaded the logo of the company, so you guys can fit that in your design as well.
Updates

Hy everybody This will be the last update for the brief. The company will focus in the beginning for mobile development only, so i would like the website design to be done in a matter that will reflect that. We will develop Orion, Andrin and Vindra applications. We will also require 3 pages: One for the home menu, one for portfolio and one for contact us. The layout should be the same ( one page scroll down ) but the design of the 3 pages different. Please readdress the brief. Hope that i provided enough information for the scope of the project.

I have uploaded the logo that you guys can use. If the logo requires small modifications you can adjust that to suit your idea as long as the logo does not change completely.

Target Market(s)

High End companies that require simplified software solutions.

Industry/Entity Type

It Company

Number of Pages Required

3 page

Requirements
Must have
• One page scroll down layout for 3 pages:
• one for home page, one for portfolio and one for contact us.
• In the portfolio page we would like to have different display options for given examples of applications ( min 3 )

```html
<!DOCTYPE html>
<html lang="en">
<head>
<meta charset="utf-8">
<title>Velquin Solutions</title>
<link href="https://fonts.googleapis.com/css2?family=Lato:ital,wght@0,400;0,700;1,400&family=Arimo:wght@400;700&display=swap" rel="stylesheet">
<style>
:root{
  --brand-blue:#2272c2;
  --brand-blue-light:#3f89d3;
  --panel-border:#5a9ada;
  --card-bg:#e6eff8;
  --ink:#222;
  --body-text:#444;
  --accent-green:#8cbf26;
  --device-grey:#6f757a;
  --white:#fff;
}
*{box-sizing:border-box;margin:0;padding:0}
html,body{width:1200px;height:1182px;overflow:hidden}
body{position:relative;background:var(--white);font-family:'Lato',sans-serif;color:var(--ink)}
.abs{position:absolute}
.header-band{left:0;top:0;width:1200px;height:600px;background:var(--brand-blue)}
.brand{left:145px;top:38px;display:flex;align-items:center;gap:14px;color:var(--white)}
.brand-dot{width:44px;height:44px;border-radius:50%;background:var(--white)}
.brand-name{font-size:33px;font-weight:700;line-height:1;white-space:nowrap}
.call{left:888px;top:24px;display:flex;align-items:center;gap:8px;color:var(--white)}
.call-label{font-size:13px;letter-spacing:2px;font-weight:700}
.call-number{font-size:19px;font-weight:700;letter-spacing:.3px}
.main-nav{left:765px;top:90px;display:flex;color:var(--white);font-size:17px;letter-spacing:.5px}
.main-nav a{color:inherit;text-decoration:none;padding:2px 8px 8px}
.main-nav a.active{font-weight:700;border-bottom:3px solid var(--white)}
.slider-frame{left:138px;top:138px;width:924px;height:402px;background:var(--white);box-shadow:0 8px 14px rgba(0,0,0,.25)}
.slide{left:148px;top:138px;width:904px;height:392px;background:linear-gradient(180deg,#f1f6ea 0%,#f8fbf3 55%,#e6efd4 100%);border:1px solid #dde6d0;overflow:hidden}
.ph{position:absolute}
.ph-bubbles{left:0;top:110px;width:250px;height:282px;background:radial-gradient(ellipse at 35% 60%,rgba(140,191,38,.75) 0%,rgba(140,191,38,.35) 45%,rgba(140,191,38,0) 72%)}
.ph-stripes{left:700px;top:0;width:204px;height:190px;background:linear-gradient(215deg,rgba(140,191,38,.9) 0%,rgba(140,191,38,.45) 45%,rgba(140,191,38,0) 80%)}
.ph-phone-a{left:74px;top:56px;width:96px;height:158px;border-radius:12px;background:linear-gradient(160deg,#3a3f44 0%,#22262a 100%)}
.ph-phone-b{left:195px;top:2px;width:138px;height:270px;border-radius:16px;background:linear-gradient(180deg,#8d9398 0%,#7aa7c8 40%,#5e6469 100%)}
.ph-phone-c{left:352px;top:77px;width:253px;height:192px;border-radius:14px;background:linear-gradient(180deg,#9aa0a5 0%,#7aa7c8 45%,#3a3e42 62%,#2a2d30 100%)}
.ph-robot{left:636px;top:108px;width:184px;height:170px;border-radius:40px 40px 16px 16px;background:radial-gradient(ellipse at 55% 45%,rgba(140,191,38,.95) 0%,rgba(140,191,38,.6) 55%,rgba(140,191,38,0) 80%)}
.slide-title{right:168px;top:432px;font-family:'Arimo',sans-serif;font-weight:700;font-size:40px;color:var(--accent-green);white-space:nowrap}
.slide-tagline{right:168px;top:480px;font-family:'Arimo',sans-serif;font-size:25px;color:#333;letter-spacing:.3px;white-space:nowrap}
.slide-arrow{top:316px;width:30px;height:44px;background:#e4e4e4;display:flex;align-items:center;justify-content:center;box-shadow:0 1px 3px rgba(0,0,0,.3)}
.service{top:540px;width:288px;height:161px;background:var(--card-bg);text-align:center}
.service-icon{width:58px;height:58px;margin:16px auto 0;background:var(--brand-blue);border-radius:6px}
.service h3{font-weight:400;font-size:19px;letter-spacing:.5px;margin-top:14px;color:var(--ink)}
.service p{font-size:14px;line-height:18px;color:var(--body-text);margin-top:7px}
.mid-band{left:0;top:730px;width:1200px;height:276px;background:linear-gradient(#f3f3f3,#fff 60%)}
.section-title{font-size:22px;font-weight:700;color:var(--ink)}
.rule{height:1px;background:#cfcfcf}
.about-art{left:147px;top:820px;width:200px;height:150px;background:radial-gradient(circle at 60% 40%,#5bb0e8 0%,#f0a040 35%,rgba(255,255,255,0) 70%)}
.about-text{left:372px;top:811px;width:360px;font-size:13.6px;line-height:19.4px;letter-spacing:.45px;color:var(--body-text);white-space:nowrap}
.about-text b{color:var(--ink)}
.news-item{left:786px;width:260px}
.news-date{font-size:17px;color:var(--ink)}
.news-text{font-size:14px;line-height:17px;color:#333;margin-top:3px}
.news-sep{left:784px;top:884px;width:250px;border-top:2px dotted #999}
.footer{left:0;top:1006px;width:1200px;height:176px;background:var(--brand-blue);color:var(--white)}
.foot-box{top:1034px;height:76px;border:1px solid var(--panel-border);background:var(--brand-blue-light);padding:6px 12px;color:var(--white)}
.foot-box h4{font-size:15px;font-weight:700}
.email-field{position:absolute;left:9px;top:35px;width:179px;height:29px;background:var(--white);color:#333;font-style:italic;font-size:11px;padding:8px}
.email-go{position:absolute;left:194px;top:35px;width:31px;height:29px;background:var(--white);display:flex;align-items:center;justify-content:center}
.contact-line{display:flex;align-items:center;gap:8px;font-size:13px;margin-top:5px}
.social{display:flex;gap:12px;margin-top:12px}
.social span{width:24px;height:24px;background:#dce9f6;border-radius:3px}
.foot-brand{left:795px;top:1050px;display:flex;align-items:center;gap:12px;color:#7fb0e3}
.foot-brand .brand-dot{background:#7fb0e3;width:40px;height:40px}
.foot-links{left:147px;top:1147px;font-size:12px;letter-spacing:.4px;color:var(--white)}
.copyright{right:150px;top:1148px;font-size:12px;letter-spacing:.4px;color:var(--white)}
</style>
</head>
<body>
<div class="abs header-band"></div>

<div class="abs brand"><span class="brand-dot"></span><span class="brand-name">Velquin Solutions</span></div>

<div class="abs call">
  <svg width="38" height="38" viewBox="0 0 38 38"><circle cx="19" cy="19" r="17" fill="none" stroke="#fff" stroke-width="2.5"/><path d="M13 10c2-1 3 0 4 3s-1 3-1 4c1 3 3 5 5 6 1 0 2-2 4-1s3 2 2 4-3 3-6 1c-5-3-9-8-10-12-1-3 0-4 2-5z" fill="#fff"/></svg>
  <div><div class="call-label">CALL US TODAY</div><div class="call-number">012-555-0187</div></div>
</div>

<nav class="abs main-nav"><a class="active" href="#">HOME</a><a href="#">ABOUT US</a><a href="#">CONACT US</a></nav>

<div class="abs slider-frame"></div>
<div class="abs slide">
  <div class="ph ph-bubbles" role="img" aria-label="Scattered green bubbles"></div>
  <div class="ph ph-stripes" role="img" aria-label="Green diagonal stripes"></div>
  <div class="ph ph-phone-a" role="img" aria-label="Dark smartphone showing a home screen"></div>
  <div class="ph ph-phone-b" role="img" aria-label="Silver smartphone showing app icons"></div>
  <div class="ph ph-phone-c" role="img" aria-label="Smartphone with slide-out keyboard"></div>
  <div class="ph ph-robot" role="img" aria-label="Green robot mascot waving"></div>
</div>
<div class="abs slide-title">Andrin Apps Development</div>
<div class="abs slide-tagline">Don't just think of the possibilities, experience it</div>
<div class="abs slide-arrow" style="left:134px"><svg width="14" height="20" viewBox="0 0 14 20"><path d="M11 2 3 10l8 8" fill="none" stroke="#222" stroke-width="3"/></svg></div>
<div class="abs slide-arrow" style="left:1037px"><svg width="14" height="20" viewBox="0 0 14 20"><path d="M3 2l8 8-8 8" fill="none" stroke="#222" stroke-width="3"/></svg></div>

<div class="abs service" style="left:148px"><div class="service-icon"></div><h3>ORION APPLICATIONS</h3><p>Larem ipsum dolor sit amet, consectetur<br>adipisicing elit, sed do eiusmod.</p></div>
<div class="abs service" style="left:456px"><div class="service-icon"></div><h3>ANDRIN APPLICATIONS</h3><p>Larem ipsum dolor sit amet, consectetur<br>adipisicing elit, sed do eiusmod.</p></div>
<div class="abs service" style="left:765px"><div class="service-icon"></div><h3>VINDRA APPLICATIONS</h3><p>Larem ipsum dolor sit amet, consectetur<br>adipisicing elit, sed do eiusmod.</p></div>

<div class="abs mid-band"></div>
<h2 class="abs section-title" style="left:150px;top:757px">ABOUT VELQUIN SOLUTIONS</h2>
<div class="abs rule" style="left:147px;top:788px;width:558px"></div>
<div class="abs about-art" role="img" aria-label="Smartphone surrounded by colourful app icons"></div>
<p class="abs about-text">Lorem ipsum dolor sit amet, this is consectetuer<br>adipiscing elit, sed diam nonummy nibh euismod<br>tincidunt ut laoreet dolore magna aliquam erat volutpat.<br>&nbsp;wisi enim ad minim veniam, quis nostrud exerci tation<br>ullamcorper suscipit lobortis nisl ut aliquip ex ea<br>commodoe &nbsp;wisi enim ad minim veniam, quis nostrud<br>exerci tation ullamcorper suscipit lobortis nisl ut aliquip<br>ex ea commodo. &nbsp;<b>Read More &gt;&gt;</b></p>

<h2 class="abs section-title" style="left:784px;top:757px">LATEST NEWS</h2>
<svg class="abs" style="left:1010px;top:764px" width="34" height="16" viewBox="0 0 34 16"><path d="M9 2 3 8l6 6M25 2l6 6-6 6" fill="none" stroke="#bbb" stroke-width="2.5"/></svg>
<div class="abs rule" style="left:780px;top:788px;width:268px"></div>
<div class="abs news-item" style="top:810px"><div class="news-date">Sep 29, 2014</div><div class="news-text">Ut wisi enim ad minim veniam, quis nostr<br>ud exerci tation ullamcorper.</div></div>
<div class="abs news-sep"></div>
<div class="abs news-item" style="top:901px"><div class="news-date">Sep 28, 2014</div><div class="news-text">Ut wisi enim ad minim veniam, quis nostr<br>ud exerci tation ullamcorper.</div></div>

<footer class="abs footer"></footer>
<div class="abs foot-box" style="left:147px;width:242px"><h4>Subscribe to Newsletter</h4><div class="email-field">Email here</div><div class="email-go"><svg width="12" height="14" viewBox="0 0 12 14"><path d="M3 2l6 5-6 5" fill="none" stroke="#2272c2" stroke-width="3"/></svg></div></div>
<div class="abs foot-box" style="left:411px;width:208px"><h4>Contact Details</h4>
  <div class="contact-line"><svg width="12" height="12" viewBox="0 0 12 12"><path d="M2 1c1-1 2 0 3 2s-1 2 0 3 2 2 3 1 2 0 3 1-1 3-3 3C5 11 1 7 1 4c0-1 0-2 1-3z" fill="#fff"/></svg>012-555-0187</div>
  <div class="contact-line"><svg width="13" height="10" viewBox="0 0 13 10"><rect x=".5" y=".5" width="12" height="9" fill="none" stroke="#fff"/><path d="M.5.5l6 5 6-5" fill="none" stroke="#fff"/></svg>info@VelquinSolution.com</div>
</div>
<div class="abs foot-box" style="left:631px;width:116px"><h4>Follow Us</h4><div class="social"><span></span><span></span><span></span></div></div>
<div class="abs foot-brand"><span class="brand-dot"></span><span class="brand-name" style="font-size:27px">Velquin Solutions</span></div>
<div class="abs foot-links">Home &nbsp;| &nbsp;About Us &nbsp;| &nbsp;Contact Us</div>
<div class="abs copyright">© 2014 &nbsp;Velquin Solutions. All Rights Reserved.</div>
</body>
</html>
```